DOVR Business Card Design Project

Company Name: DOVR (Dove Operational Versatile Resources) JLT.
Office Address: Office No 218, Saffron Crest Tower, Palmera Bay Towers, Dubai, U.A.E
Company line of business:
1) Currently we have a POS solution for retail outlets like duty free shops, supermarkets, department stores etc... The solution is deployed in Harbor Gate Retail on 350 POS and in Coralline Port Retail on 100 POS. So our main line of business is the deployment of this solution in retail outlets locally or regionally. We have already deployed the solution in India and Australia.
2) Integration of other third party POS systems with an online credit authorization netwotk in the UAE. This will enable POS applications to connect directly to the acquiring banks without needing an EFT terminal like Paxoline or Tramodex. The credit card payment is completed at the POS.
3) Other solutions that are targeting retail outlets like mobile POS, queue busting solutions, stock taking solutions using hand held devices, transaction capture systems, etc...
4) Other IT services like support of call center solutions from Bramwell Systems and development of new solutions as per customer requirements.
We need a business card design for the company. We don't have any specific requirements and will eave up to the designers to come up with creative designs. At the moment we still don't have a letter head design and the only thing that we have is the company logo that we will upload shortly.
Updates
Dear All,
I just uploaded the logo source files. I am sorry for the delay.
Regards
Tarek Demirci
I would like the business cards to have the following details:
Company Tel No
Company Fax No
Company Website Address
Employee Name
Employee Title
Employee Mobile Number
Employee Email Address

```html
<!DOCTYPE html>
<html lang="en">
<head>
<meta charset="utf-8">
<title>DOVR Business Card</title>
<link rel="stylesheet" href="https://fonts.googleapis.com/css2?family=Arimo:wght@400;700&family=Tinos:ital,wght@1,700&display=swap">
<style>
  :root {
    --backdrop: #e9e6e1;
    --card: #ffffff;
    --blue-deep: #0a5aa6;
    --blue-light: #2ea3e0;
    --ink: #111111;
    --navy: #1b2b4f;
    --icon: #1f7cc4;
  }
  * { margin: 0; padding: 0; box-sizing: border-box; }
  html, body { width: 1200px; height: 944px; overflow: hidden; }
  body {
    background: var(--backdrop);
    font-family: "Arimo", Arial, sans-serif;
    color: var(--ink);
    position: relative;
  }
  .card {
    position: absolute;
    left: 290px;
    width: 620px;
    height: 340px;
    background: var(--card);
    box-shadow: 0 6px 18px rgba(0,0,0,0.25);
    overflow: hidden;
  }
  .card--front { top: 70px; }
  .card--back { top: 500px; }

  .band {
    position: absolute;
    left: 0;
    width: 100%;
  }
  .card--front .band--top {
    top: 0; height: 100px;
    background: linear-gradient(90deg, var(--blue-deep), var(--blue-light));
    border-bottom-left-radius: 0 0;
  }
  .card--front .band--bottom {
    bottom: 0; height: 90px;
    background: linear-gradient(90deg, var(--blue-light), var(--blue-deep));
  }
  .card--back .band--bottom {
    bottom: 0; height: 72px;
    background: linear-gradient(90deg, var(--blue-light), var(--blue-deep));
  }
  .card__tab {
    position: absolute;
    left: 0; top: 135px;
    width: 6px; height: 80px;
    background: var(--blue-deep);
  }

  .brand {
    position: absolute;
    display: flex;
    align-items: center;
    gap: 14px;
  }
  .brand__dot {
    border-radius: 50%;
    background: var(--blue-deep);
  }
  .brand__name {
    font-weight: 700;
    color: var(--ink);
    letter-spacing: 2px;
    line-height: 1;
  }
  .card--front .brand { left: 215px; top: 135px; }
  .card--front .brand__name { font-size: 66px; }
  .card--front .brand__dot { width: 48px; height: 48px; }
  .card--back .brand { left: 40px; top: 40px; }
  .card--back .brand__name { font-size: 44px; }
  .card--back .brand__dot { width: 32px; height: 32px; }

  .person {
    position: absolute;
    right: 30px;
    top: 58px;
    text-align: center;
  }
  .person__name {
    font-family: "Tinos", "Times New Roman", serif;
    font-style: italic;
    font-weight: 700;
    font-size: 17px;
    color: var(--navy);
  }
  .person__title { font-size: 14px; margin-top: 3px; }

  .contacts {
    position: absolute;
    left: 30px;
    top: 136px;
    list-style: none;
    font-size: 14px;
  }
  .contacts li {
    display: flex;
    align-items: center;
    gap: 7px;
    height: 19px;
  }
  .contacts li:nth-child(-n+3) { padding-left: 8px; }
  .contacts li:nth-child(4) { padding-left: 2px; }
  .icon { width: 13px; height: 13px; flex: none; color: var(--icon); }

  .address {
    position: absolute;
    left: 250px;
    top: 148px;
    font-size: 14px;
    font-style: normal;
    line-height: 18px;
    display: flex;
    gap: 6px;
  }
  .address__lines span { display: block; }
  .address__lines span + span { padding-left: 18px; }
</style>
</head>
<body>

<section class="card card--front" aria-label="Business card front">
  <div class="band band--top" role="img" aria-label="Blue wave band with red swoosh stripe"></div>
  <div class="band band--bottom" role="img" aria-label="Blue wave band with lime and yellow swoosh stripe"></div>
  <div class="brand">
    <span class="brand__dot"></span>
    <span class="brand__name">DOVR</span>
  </div>
</section>

<section class="card card--back" aria-label="Business card back">
  <div class="band band--bottom" role="img" aria-label="Blue wave band with red, yellow and lime swoosh stripes"></div>
  <span class="card__tab"></span>

  <div class="brand">
    <span class="brand__dot"></span>
    <span class="brand__name">DOVR</span>
  </div>

  <div class="person">
    <p class="person__name">Tarek Demirci</p>
    <p class="person__title">Managing Director</p>
  </div>

  <ul class="contacts">
    <li>
      <svg class="icon" viewBox="0 0 16 16" aria-label="Telephone"><circle cx="8" cy="8" r="7" fill="none" stroke="currentColor" stroke-width="1.6"/><path d="M5.5 4.5 L7 4.5 L7.5 6.5 L6.5 7.2 C7 8.4 7.8 9.2 9 9.7 L9.7 8.7 L11.5 9.2 L11.5 10.7 C8 11 5 8 5.5 4.5 Z" fill="currentColor"/></svg>
      <span>(+97) 9XXX XXXX</span>
    </li>
    <li>
      <svg class="icon" viewBox="0 0 16 16" aria-label="Fax"><rect x="4" y="1.5" width="8" height="5" fill="none" stroke="currentColor" stroke-width="1.4"/><rect x="1" y="6" width="14" height="6" rx="1" fill="currentColor"/><rect x="4" y="10" width="8" height="5" fill="#fff" stroke="currentColor" stroke-width="1.4"/></svg>
      <span>(+97) 9XXX XXXX</span>
    </li>
    <li>
      <svg class="icon" viewBox="0 0 16 16" aria-label="Mobile"><rect x="4.5" y="1" width="7" height="14" rx="1.5" fill="currentColor"/><rect x="6" y="3" width="4" height="6" fill="#fff"/></svg>
      <span>(+97) 500 614 282</span>
    </li>
    <li>
      <svg class="icon" viewBox="0 0 16 16" aria-label="Email"><rect x="1" y="3" width="14" height="10" fill="none" stroke="currentColor" stroke-width="1.5"/><path d="M1 3 L8 9 L15 3" fill="none" stroke="currentColor" stroke-width="1.5"/></svg>
      <span>tarekdemirci@dovr.com</span>
    </li>
    <li>
      <svg class="icon" viewBox="0 0 16 16" aria-label="Website"><circle cx="8" cy="8" r="6.5" fill="none" stroke="currentColor" stroke-width="1.4"/><ellipse cx="8" cy="8" rx="3" ry="6.5" fill="none" stroke="currentColor" stroke-width="1.2"/><path d="M1.5 8 H14.5" stroke="currentColor" stroke-width="1.2"/></svg>
      <span>www.dovr.com</span>
    </li>
  </ul>

  <address class="address">
    <svg class="icon" viewBox="0 0 16 16" aria-label="Address"><path d="M8 1.5 L15 8 H13 V14.5 H9.5 V10.5 H6.5 V14.5 H3 V8 H1 Z" fill="currentColor"/></svg>
    <span class="address__lines">
      <span>Office No 218, Saffron Crest Tower</span>
      <span>Palmera Bay Towers,</span>
      <span>Dubai, U.A.E</span>
    </span>
  </address>
</section>

</body>
</html>
```